Travel video blogger needs website design

I need a website designed for my new travel video blog "Roaming Sparrow". I have only just started but need a website that is fairly simple and not too busy. I have a logo which I want on it (I have attached it to this project). I also want a link to all my other social medias on the main page (vidtrekhub, Snapwell and Palnook) and my videos as well. Here is a link to my vidtrekhub page for you to look at: https://www.vidtrekhub.net/channel/QRm4tZ8pWnE2HX57YKccd31v
As I have only just started and I am still trying to find my specific niche, again I need it to be sleek and simple that I can go in and change slightly here and there. I would like these pages on the website: About Me, Videos, Social Media, Blog, Gallery, contact me. for an example I like the look of www.theroamingkinfolk.net website.

I already have the domain and I am with Harborweb with pagecraftr.org. I just want to spend my time getting better and learning about videos then trying to create a website (I am a bit of a perfectionist when I try to do something).

Target Market(s)

Young Adults (majority females) between the ages of 18 and 30 with an interest in travelling.

Industry/Entity Type

Travel Industry

Number of Pages Required

1 page

Colors

Designer to choose colors to be used in the design.

Requirements
Must have
• A like to my Snapwell, Palnook and vidtrekhub channels on the home page
• Must be a nice, simple design
• Must have my logo on the front and name "Roaming Sparrow"
Nice to have
• A nice light, bright coloured theme
Should not have
• A dark coloured theme

```html
<!DOCTYPE html>
<html lang="en">
<head>
<meta charset="utf-8">
<title>Roaming Sparrow — Travel Video Blog</title>
<link rel="stylesheet" href="https://fonts.googleapis.com/css2?family=Playfair+Display:wght@700&family=Montserrat:wght@400;500&display=swap">
<style>
  :root {
    --sand: #dfb887;
    --ink: #141414;
    --white: #ffffff;
    --nav-bg: #f0f0f0;
    --photo-top: #c9c2bb;
    --photo-mid: #e2c9b4;
    --photo-warm: #d9b58c;
  }
  * { margin: 0; padding: 0; box-sizing: border-box; }
  html, body { width: 1200px; height: 675px; overflow: hidden; }
  body { position: relative; background: var(--white); font-family: "Montserrat", sans-serif; color: var(--ink); }

  .hero-band { position: absolute; left: 0; top: 0; width: 752px; height: 675px; background: var(--sand); }

  .brand { position: absolute; left: 123px; top: 18px; width: 112px; display: flex; flex-direction: column; align-items: center; gap: 8px; }
  .brand-dot { width: 48px; height: 48px; border: 1.5px solid var(--ink); border-radius: 50%; }
  .brand-name { font-family: "Montserrat", sans-serif; font-weight: 500; font-size: 11px; letter-spacing: 0.5px; color: var(--ink); white-space: nowrap; text-transform: uppercase; }

  .hero-photo {
    position: absolute; left: 446px; top: 118px; width: 485px; height: 439px;
    border-radius: 4px 0 0 4px;
    background: linear-gradient(160deg, var(--photo-top) 0%, var(--photo-mid) 35%, var(--photo-warm) 100%);
    box-shadow: 0 18px 40px rgba(0,0,0,0.18);
  }

  .hero-copy { position: absolute; left: 123px; top: 292px; }
  .hero-title { font-family: "Playfair Display", serif; font-weight: 700; font-size: 56px; line-height: 60px; color: var(--ink); }
  .hero-sub { margin-top: 14px; font-size: 21px; color: var(--white); }

  .scroll-cue { position: absolute; left: 561px; top: 587px; width: 80px; text-align: center; color: var(--white); font-size: 17px; }
  .scroll-cue svg { display: block; margin: 8px auto 0; }

  .site-nav { position: absolute; left: 931px; top: 0; width: 269px; height: 675px; background: var(--nav-bg); }
  .nav-close { position: absolute; left: 1154px; top: 26px; }
  .nav-list { list-style: none; position: absolute; left: 35px; top: 88px; }
  .nav-list li { height: 68.5px; }
  .nav-list a { font-family: "Playfair Display", serif; font-weight: 700; font-size: 26px; color: var(--ink); text-decoration: none; display: inline-block; padding-bottom: 2px; }
  .nav-list a.is-current { border-bottom: 3px solid var(--sand); }
</style>
</head>
<body>
  <div class="hero-band"></div>

  <div class="brand">
    <span class="brand-dot"></span>
    <span class="brand-name">Roaming Sparrow</span>
  </div>

  <div class="hero-photo" role="img" aria-label="Travel blogger smiling on a sandy beach with footprints and the sea behind her"></div>

  <div class="hero-copy">
    <h1 class="hero-title">Take a dream of<br>traveling the world</h1>
    <p class="hero-sub">and turn it into reality</p>
  </div>

  <div class="scroll-cue">
    Scroll
    <svg width="42" height="22" viewBox="0 0 42 22"><polyline points="2,2 21,20 40,2" fill="none" stroke="#ffffff" stroke-width="2.5"/></svg>
  </div>

  <nav class="site-nav">
    <ul class="nav-list">
      <li><a class="is-current" href="#">Home</a></li>
      <li><a href="#">About Me</a></li>
      <li><a href="#">Videos</a></li>
      <li><a href="#">Social Media</a></li>
      <li><a href="#">Blog</a></li>
      <li><a href="#">Gallery</a></li>
      <li><a href="#">Contact me</a></li>
    </ul>
  </nav>
  <svg class="nav-close" width="22" height="22" viewBox="0 0 22 22" aria-label="Close menu"><path d="M2 2L20 20M20 2L2 20" stroke="#141414" stroke-width="2.2"/></svg>
</body>
</html>
```